BRVE branded stationary template

We need associated stationary to accompany our new logo.

The stationary design will be used on business cards, presentation slides and document templates so needs to be provided in an EPS format so that we can adapt it. The design MUST BE ADAPTABLE.

The logo colour is #4a4195 or RGB 85/68/141. Associated colours that can be used in this stationary should compliment this colour. Other colour choices - the preference would be dark and light purples, blues, black and greys. Done how you see fit.

We want the stationary to compliment the overall design of the logo, so clean sharp lines are what we are looking for. It doesn't need to be overly intricate in design - something simple that compliments the look and feel of the logo is what we want. More focused on lines and shapes around the stationary, not any additional logos or pictures.

Target Market(s)

UK housing providers

Industry/Entity Type

Business

Font styles to use
Sans Serif

Requirements
Must have
• Clean sharp appearance, nothing overly elaborate.

```html
<!DOCTYPE html>
<html lang="en">
<head>
<meta charset="utf-8">
<title>BRVE Presentation Templates</title>
<link href="https://fonts.googleapis.com/css2?family=Open+Sans:wght@400;600;700&family=Raleway:wght@300;400&display=swap" rel="stylesheet">
<style>
  :root {
    --brand: #4a4195;
    --purple: #665eaa;
    --purple-text: #5a51a4;
    --sheet: #f7f7f7;
    --band-grey: #c8c8c8;
    --rule: #9a9a9a;
    --ink: #333;
    --page-bg: #e9e9ec;
    --c-comm: #7cae4a;
    --c-pic: #1f6b86;
    --c-res: #2e9b8a;
    --c-qual: #e8bb4a;
  }
  * { margin: 0; padding: 0; box-sizing: border-box; }
  html, body { width: 1200px; height: 974px; overflow: hidden; }
  body { background: var(--page-bg); font-family: "Open Sans", sans-serif; position: relative; }

  .slide { position: absolute; width: 470px; height: 347px; background: var(--sheet); overflow: hidden; }
  .slide--cover { left: 88px; top: 78px; }
  .slide--team { left: 637px; top: 78px; }
  .slide--chart { left: 88px; top: 504px; }
  .slide--closing { left: 637px; top: 504px; }

  .hero { position: absolute; left: 0; top: 0; width: 100%; height: 206px; background: var(--purple); }
  .title-band { position: absolute; left: 0; top: 206px; width: 100%; height: 79px; background: var(--sheet); }
  .foot-band { position: absolute; left: 0; top: 285px; width: 100%; height: 62px; background: var(--band-grey); }

  .brand { position: absolute; display: flex; flex-direction: column; align-items: flex-start; }
  .brand__row { display: flex; align-items: center; gap: 6px; }
  .brand__mark { width: 7px; height: 7px; background: var(--purple-text); }
  .brand__name { font-weight: 700; color: var(--purple-text); letter-spacing: 0.5px; line-height: 1; }
  .brand__tag { color: var(--purple-text); white-space: nowrap; line-height: 1.2; }

  .slide--cover .brand { left: 42px; top: 236px; }
  .slide--cover .brand__name { font-size: 25px; }
  .slide--cover .brand__tag { font-size: 7.5px; margin-top: 3px; margin-left: 4px; }
  .cover__title { position: absolute; right: 50px; top: 232px; font-family: "Raleway", sans-serif; font-weight: 300; font-size: 21px; color: var(--purple-text); letter-spacing: 0.3px; line-height: 1.1; }
  .cover__subtitle { position: absolute; right: 50px; top: 258px; font-family: "Raleway", sans-serif; font-weight: 300; font-size: 10px; color: #8a8a8a; letter-spacing: 0.4px; }
  .cover__url { position: absolute; left: 39px; top: 310px; font-size: 7.5px; color: #fff; }

  .header .brand { left: 28px; top: 27px; }
  .header .brand__name { font-size: 15px; }
  .header .brand__mark { width: 5px; height: 5px; }
  .header .brand__tag { font-size: 4.5px; margin-top: 2px; margin-left: 3px; }
  .header__title { position: absolute; right: 50px; top: 33px; font-family: "Raleway", sans-serif; font-weight: 400; font-size: 12px; color: var(--purple-text); letter-spacing: 0.3px; line-height: 16px; }
  .header__page { position: absolute; right: 27px; top: 33px; width: 16px; height: 16px; background: var(--band-grey); color: #fff; font-size: 11px; text-align: center; line-height: 16px; }
  .header__rule { position: absolute; left: 26px; right: 26px; top: 53px; height: 1px; background: var(--rule); }

  .base-bar { position: absolute; left: 0; bottom: 0; width: 100%; height: 7px; background: var(--purple); border-top: 1px solid #d2d2d6; }

  .team__intro { position: absolute; left: 26px; right: 26px; top: 88px; font-size: 6.8px; line-height: 10.5px; color: #666; text-align: center; }
  .member { position: absolute; top: 127px; width: 82px; }
  .member__photo { width: 82px; height: 82px; background: linear-gradient(160deg, #a9a9a9, #6f6f6f 60%, #4d4d4d); }
  .member__name { margin-top: 10px; font-size: 9.5px; font-weight: 700; color: var(--ink); }
  .member__role { font-size: 7.5px; color: #9a9a9a; margin-top: 1px; }
  .member__bio { margin-top: 10px; font-size: 5.4px; line-height: 7.4px; color: #777; width: 76px; }

  .chart { position: absolute; left: 0; top: 0; }
  .chart text { font-family: "Open Sans", sans-serif; fill: #777; }
  .chart__note { position: absolute; left: 30px; right: 30px; top: 252px; font-size: 5.6px; line-height: 11.2px; color: #777; text-align: center; }

  .thanks { position: absolute; left: 0; top: 93px; width: 100%; text-align: center; color: #fff; }
  .thanks__main { font-size: 22px; letter-spacing: 0.4px; }
  .thanks__sub { font-size: 13px; margin-top: 3px; letter-spacing: 0.4px; }
  .slide--closing .brand { left: 0; width: 100%; top: 230px; align-items: center; }
  .slide--closing .brand__name { font-size: 23px; }
  .slide--closing .brand__tag { font-size: 7px; margin-top: 3px; }
  .contact { position: absolute; left: 0; top: 312px; width: 100%; display: flex; justify-content: center; align-items: center; gap: 6px; font-size: 6.6px; color: #fff; }
  .contact svg { width: 7px; height: 7px; }
  .contact span { margin-right: 6px; }
</style>
</head>
<body>

<section class="slide slide--cover">
  <div class="hero"></div>
  <div class="title-band"></div>
  <div class="foot-band"></div>
  <div class="brand">
    <div class="brand__row"><span class="brand__mark"></span><span class="brand__name">BRVE</span></div>
    <div class="brand__tag">building better places together</div>
  </div>
  <h1 class="cover__title">TITLES GOES HERE</h1>
  <p class="cover__subtitle">SUBTITLES GOES HERE</p>
  <p class="cover__url">www.BRVE.com</p>
</section>

<section class="slide slide--team">
  <div class="header">
    <div class="brand">
      <div class="brand__row"><span class="brand__mark"></span><span class="brand__name">BRVE</span></div>
      <div class="brand__tag">building better places together</div>
    </div>
    <h2 class="header__title">TITLES GOES HERE</h2>
    <span class="header__page">2</span>
    <div class="header__rule"></div>
  </div>
  <p class="team__intro">Simply dummy text of the printing and typesetting industry when an unknown printer took a galley of type and scrambled it to make a type specimen book unknown printer took a galley of type and scrambled.</p>

  <div class="member" style="left:34px">
    <div class="member__photo" role="img" aria-label="Portrait photo of team member"></div>
    <div class="member__name">Owen Hartley</div>
    <div class="member__role">Director</div>
    <p class="member__bio">Simply dummy text of the printing and typesetting industry when an unknown printer took.</p>
  </div>
  <div class="member" style="left:139px">
    <div class="member__photo" role="img" aria-label="Portrait photo of team member"></div>
    <div class="member__name">Nina Calloway</div>
    <div class="member__role">Graphic Designer</div>
    <p class="member__bio">Simply dummy text of the printing and typesetting industry when an unknown printer took.</p>
  </div>
  <div class="member" style="left:245px">
    <div class="member__photo" role="img" aria-label="Portrait photo of team member"></div>
    <div class="member__name">Reid Marston</div>
    <div class="member__role">Programmer</div>
    <p class="member__bio">Simply dummy text of the printing and typesetting industry when an unknown printer took.</p>
  </div>
  <div class="member" style="left:350px">
    <div class="member__photo" role="img" aria-label="Portrait photo of team member"></div>
    <div class="member__name">Elena</div>
    <div class="member__role">Marketing</div>
    <p class="member__bio">Simply dummy text of the printing and typesetting industry when an unknown printer took.</p>
  </div>
  <div class="base-bar"></div>
</section>

<section class="slide slide--chart">
  <div class="header">
    <div class="brand">
      <div class="brand__row"><span class="brand__mark"></span><span class="brand__name">BRVE</span></div>
      <div class="brand__tag">building better places together</div>
    </div>
    <h2 class="header__title">TITLES GOES HERE</h2>
    <span class="header__page">3</span>
    <div class="header__rule"></div>
  </div>

  <svg class="chart" width="470" height="347" viewBox="0 0 470 347" aria-label="Line chart of four series from January to June">
    <g stroke="#e3e3e3" stroke-width="0.6">
      <line x1="61" y1="116" x2="415" y2="116"/><line x1="61" y1="128.3" x2="415" y2="128.3"/>
      <line x1="61" y1="140.5" x2="415" y2="140.5"/><line x1="61" y1="152.8" x2="415" y2="152.8"/>
      <line x1="61" y1="165" x2="415" y2="165"/><line x1="61" y1="177.3" x2="415" y2="177.3"/>
      <line x1="61" y1="189.5" x2="415" y2="189.5"/><line x1="61" y1="201.8" x2="415" y2="201.8"/>
      <line x1="415" y1="116" x2="415" y2="214"/>
    </g>
    <line x1="61" y1="116" x2="61" y2="214" stroke="#bbb" stroke-width="0.6"/>
    <line x1="61" y1="214" x2="415" y2="214" stroke="#bbb" stroke-width="0.6"/>
    <g font-size="4.5" text-anchor="end">
      <text x="58" y="118">800</text><text x="58" y="130">700</text><text x="58" y="142">600</text>
      <text x="58" y="154">500</text><text x="58" y="167">400</text><text x="58" y="179">300</text>
      <text x="58" y="191">200</text><text x="58" y="203">100</text><text x="58" y="216">0</text>
    </g>
    <g font-size="4.5" text-anchor="middle">
      <text x="93" y="222">Jan</text><text x="151" y="222">Feb</text><text x="210" y="222">Mar</text>
      <text x="269" y="222">April</text><text x="327" y="222">May</text><text x="386" y="222">Jun</text>
    </g>

    <polyline fill="none" stroke="var(--c-qual)" stroke-width="0.8" points="93,195.6 151,189.5 210,177.3 269,207.9 327,201.8 386,152.8"/>
    <polyline fill="none" stroke="var(--c-comm)" stroke-width="0.8" points="93,201.8 151,165 210,195.6 269,185.8 327,158.9 386,177.3"/>
    <polyline fill="none" stroke="var(--c-res)" stroke-width="0.8" points="93,185.8 151,195.6 210,165 269,140.5 327,128.3 386,165"/>
    <polyline fill="none" stroke="var(--c-pic)" stroke-width="0.8" stroke-opacity="0.8" points="93,140.5 151,145.4 210,165 269,165 327,189.5 386,143"/>

    <g fill="var(--c-qual)">
      <rect x="90.5" y="193.1" width="5" height="5"/><rect x="148.5" y="187" width="5" height="5"/>
      <rect x="207.5" y="174.8" width="5" height="5"/><rect x="266.5" y="205.4" width="5" height="5"/>
      <rect x="324.5" y="199.3" width="5" height="5"/><rect x="383.5" y="150.3" width="5" height="5"/>
    </g>
    <g fill="var(--c-comm)">
      <circle cx="93" cy="201.8" r="2.4"/><circle cx="151" cy="165" r="2.4"/><circle cx="210" cy="195.6" r="2.4"/>
      <circle cx="269" cy="185.8" r="2.4"/><circle cx="327" cy="158.9" r="2.4"/><circle cx="386" cy="177.3" r="2.4"/>
    </g>
    <g fill="var(--c-res)">
      <path d="M93 183.1l2.6 4.4h-5.2z"/><path d="M151 192.9l2.6 4.4h-5.2z"/><path d="M210 162.3l2.6 4.4h-5.2z"/>
      <path d="M269 137.8l2.6 4.4h-5.2z"/><path d="M327 125.6l2.6 4.4h-5.2z"/><path d="M386 162.3l2.6 4.4h-5.2z"/>
    </g>
    <g fill="var(--c-pic)">
      <path d="M93 138l2.5 2.5-2.5 2.5-2.5-2.5z"/><path d="M151 142.9l2.5 2.5-2.5 2.5-2.5-2.5z"/>
      <path d="M210 162.5l2.5 2.5-2.5 2.5-2.5-2.5z"/><path d="M269 162.5l2.5 2.5-2.5 2.5-2.5-2.5z"/>
      <path d="M327 187l2.5 2.5-2.5 2.5-2.5-2.5z"/><path d="M386 140.5l2.5 2.5-2.5 2.5-2.5-2.5z"/>
    </g>

    <g font-size="4">
      <line x1="120" y1="231" x2="130" y2="231" stroke="var(--c-comm)" stroke-width="0.8"/><circle cx="125" cy="231" r="1.3" fill="var(--c-comm)"/>
      <text x="132" y="232.5">Communication</text>
      <line x1="206" y1="231" x2="216" y2="231" stroke="var(--c-pic)" stroke-width="0.8"/><path d="M211 229.6l1.4 1.4-1.4 1.4-1.4-1.4z" fill="var(--c-pic)"/>
      <text x="218" y="232.5">Pictures</text>
      <line x1="275" y1="231" x2="285" y2="231" stroke="var(--c-res)" stroke-width="0.8"/><path d="M280 229.5l1.5 2.5h-3z" fill="var(--c-res)"/>
      <text x="287" y="232.5">Research</text>
      <line x1="345" y1="231" x2="355" y2="231" stroke="var(--c-qual)" stroke-width="0.8"/><rect x="348.7" y="229.7" width="2.6" height="2.6" fill="var(--c-qual)"/>
      <text x="357" y="232.5">Quality</text>
    </g>
  </svg>

  <p class="chart__note">There are many variations of passages of Lorem Ipsum available, but the majority have suffered alteration in some form, by injected humor, or randomized words which don't look even slightly believable. If you are going to use a passage of Lorem Ipsum, you need to be sure there isn't anything embarrassing hidden in the middle of text.</p>
  <div class="base-bar"></div>
</section>

<section class="slide slide--closing">
  <div class="hero"></div>
  <div class="title-band"></div>
  <div class="foot-band"></div>
  <div class="thanks">
    <p class="thanks__main">THANK YOU VERY MUCH</p>
    <p class="thanks__sub">FOR YOUR VALUEABLE TIME</p>
  </div>
  <div class="brand">
    <div class="brand__row"><span class="brand__mark"></span><span class="brand__name">BRVE</span></div>
    <div class="brand__tag">building better places together</div>
  </div>
  <div class="contact">
    <span>48 Linden Park Rd. Ashbury, AB1 2CD</span>
    <svg viewBox="0 0 10 10" aria-hidden="true"><rect width="10" height="10" rx="1.5" fill="#fff"/><path d="M3 2.5l1.2 1.3-.7.9c.5 1 1.1 1.6 2 2l.9-.7 1.3 1.2-.8 1C4.8 8 2.2 5.4 2 3.3z" fill="var(--band-grey)"/></svg>
    <span>555-210-4800</span>
    <svg viewBox="0 0 10 10" aria-hidden="true"><rect width="10" height="10" rx="1.5" fill="#fff"/><rect x="3" y="2" width="4" height="2" fill="var(--band-grey)"/><rect x="2" y="4.5" width="6" height="2.5" fill="var(--band-grey)"/><rect x="3" y="7" width="4" height="1.2" fill="var(--band-grey)"/></svg>
    <span>555-210-4900</span>
    <svg viewBox="0 0 10 10" aria-hidden="true"><rect width="10" height="10" rx="1.5" fill="#fff"/><circle cx="5" cy="5" r="3" fill="none" stroke="var(--band-grey)" stroke-width="0.8"/><line x1="2" y1="5" x2="8" y2="5" stroke="var(--band-grey)" stroke-width="0.7"/></svg>
    <span>www.BRVE.com</span>
  </div>
</section>

</body>
</html>
```